interior designer/stylist looking for a letter press business card to reflect the stylish work

Hello Designers,
I need a business card design for an company called Halvard Interior Design. I'm aiming at the high end residential and private client market in London providing sleek simple interiors. I'd like my business card to be tackboard worthy and expensive looking, i want people to pin it and for it to have a sought after look, and want prospective customers to hire me as their interior designer as my card is so beautiful.
I love letter press design. I also like the use of colour/foil on the edge.
Colour combos & general things I like -
Black and White
Navy Blue and Gold
Neutral colours (muted palette of greys whites navys beiges)
White Marble & brass
Morvane (fashion designer)
....also open to other suggestions....
Please dont take the pink in the attached photos too literally. i'd like the card to look more masculine than feminine.
I'd like Halvard on one side in one font, with interior design underneath so one word will make the statement....... unless anyone has any other ideas, open to suggestions.
I'd like a really simple font and for the whole card to look very graphic.
my details -
Petra Quillby
Interior Designer & Stylist
email petra@halvardinteriordesign.co.uk
phone +447813554019
website wwww.halvardinteriordesign.co.uk
GO GO GO!! EXCITED TO SEE THE OUTCOME!!
x L
Target Market(s)
High End Residential and private clients
Industry/Entity Type
Business
Contact Information for Business Card
Halvard Interior Design & Styling
Petra Quillby
phone +447813554019

```html
<!DOCTYPE html>
<html lang="en">
<head>
<meta charset="utf-8">
<title>Halvard Interior Design – Business Card</title>
<link rel="stylesheet" href="https://fonts.googleapis.com/css2?family=Courier+Prime:wght@400;700&family=Open+Sans:wght@700&display=swap">
<style>
  :root {
    --backdrop: #bdbdbd;
    --card-front: #3f5f58;
    --card-back: #202b28;
    --ink-copper: #e2876f;
  }
  html, body {
    margin: 0;
    padding: 0;
    overflow: hidden;
  }
  .canvas {
    position: relative;
    width: 1200px;
    height: 1000px;
    background: var(--backdrop);
    overflow: hidden;
  }
  .card {
    position: absolute;
    width: 735px;
    height: 420px;
    color: var(--ink-copper);
    text-align: center;
  }
  .card--details {
    left: 48px;
    top: 61px;
    background: var(--card-front);
    font-family: "Courier Prime", "Courier New", monospace;
  }
  .card--brand {
    left: 416px;
    top: 518px;
    background: var(--card-back);
    font-family: "Open Sans", Arial, sans-serif;
    font-weight: 700;
  }
  .person {
    position: absolute;
    left: 0;
    right: 0;
    top: 150px;
  }
  .person__name {
    margin: 0;
    font-size: 33px;
    font-weight: 400;
    line-height: 1;
    letter-spacing: 1px;
  }
  .person__role {
    margin: 6px 0 0;
    font-size: 19px;
    font-weight: 700;
    line-height: 1;
  }
  .contact {
    position: absolute;
    left: 0;
    right: 0;
    top: 298px;
    margin: 0;
    padding: 0;
    list-style: none;
    font-size: 19px;
    font-weight: 700;
    line-height: 22px;
  }
  .brand {
    position: absolute;
    left: 0;
    right: 0;
    top: 164px;
  }
  .brand__name {
    margin: 0;
    font-size: 58px;
    line-height: 1;
    letter-spacing: 0.5px;
  }
  .brand__tagline {
    margin: 4px 0 0;
    font-size: 27px;
    line-height: 1;
  }
</style>
</head>
<body>
  <main class="canvas">
    <section class="card card--details" aria-label="Business card front">
      <div class="person">
        <h1 class="person__name">Petra Quillby</h1>
        <p class="person__role">Interior Designer and Stylist</p>
      </div>
      <ul class="contact">
        <li class="contact__phone">+447813554019</li>
        <li class="contact__email">petra@halvardinteriordesign.co.uk</li>
        <li class="contact__web">www.halvardinteriordesign.co.uk</li>
      </ul>
    </section>

    <section class="card card--brand" aria-label="Business card back">
      <div class="brand">
        <p class="brand__name">HALVARD</p>
        <p class="brand__tagline">INTERIOR DESIGN</p>
      </div>
    </section>
  </main>
</body>
</html>
```